Quendra - Clear Spirit Cosmetics

Please design a logo and business cards for new food supplements, cosmetics and herbal fixatives. The products are produced ecologically and biologically in the South Tyrol and Trentino alps. The products are pure and noble. Quendra = pure vitality Colors Background: dark or black matt (soft touch) Logodesign: powerful, elegant, violet with glossy foil The logo and design should convey warmth, passion and the 6th sense, you should get the impression that you can smell the herbal odor , Logo and business cards for new food supplements, cosmetics and herbal fixatives. The products are produced ecologically and biologically in the South Tyrol and Trentino alps. The products are pure and noble. Quendra = pure vitality Colors Background: dark or black matt (softtouch) Logodesign: powerful elegant violet with glossy foil The logo and design is meant to convey warmth, passion and the 6th sense, you should get the impression that you can smell the herbal perfume.

Target Market(s)

Food, food supplements, vitality, health

Contact Information for Business Card

Please provide an elegant darf design that is puristic, but has a very good logo design
Elegantes dunkles design, puristisch

Logo Text

Quendra - clear Spirit

Colors
6b449b

Requirements
Must have
• SVG Files Alpha channel for foil embossing High-quality design
Nice to have
• Pure elegance
Should not have
• to colorful colors

```html
<!DOCTYPE html>
<html lang="en">
<head>
<meta charset="utf-8">
<title>Quendra – Business Card</title>
<link href="https://fonts.googleapis.com/css2?family=Work+Sans:wght@300;400;500&display=swap" rel="stylesheet">
<style>
  :root {
    --stage: #1c1c1e;
    --violet: #6b449b;
    --paper: #ffffff;
    --ink: #2b2b2e;
    --ink-soft: #4a4a4f;
    --rule: #8a6bb8;
  }
  * { box-sizing: border-box; margin: 0; padding: 0; }
  html, body {
    width: 1200px; height: 852px; overflow: hidden;
    background: var(--stage);
    font-family: "Work Sans", Arial, sans-serif;
  }
  .stage {
    position: relative; width: 1200px; height: 852px;
    display: flex; align-items: center; justify-content: center; gap: 50px;
  }
  .card {
    position: relative; width: 540px; height: 310px;
    border-radius: 18px; overflow: hidden;
  }
  .card--front { background: var(--violet); display: flex; align-items: center; justify-content: center; }
  .card--back { background: var(--paper); }

  .brand { display: flex; flex-direction: column; align-items: center; gap: 16px; }
  .brand__mark { width: 52px; height: 52px; border-radius: 50%; background: var(--paper); }
  .brand__name {
    font-weight: 400; font-size: 40px; letter-spacing: 7px; line-height: 1; color: var(--paper);
  }
  .card--back .brand { position: absolute; left: 40px; top: 40px; gap: 14px; }
  .card--back .brand__mark { background: var(--violet); width: 44px; height: 44px; }
  .card--back .brand__name { color: var(--ink); font-size: 32px; letter-spacing: 5px; }

  .holder { position: absolute; right: 36px; top: 112px; text-align: right; }
  .holder__name { font-size: 20px; font-weight: 400; color: var(--violet); letter-spacing: 0.5px; line-height: 24px; }
  .holder__role { font-size: 12px; font-weight: 300; color: var(--ink-soft); line-height: 16px; }

  .divider { position: absolute; left: 36px; right: 36px; top: 166px; height: 1px; background: var(--rule); }

  .contacts { position: absolute; left: 40px; top: 196px; list-style: none; }
  .contacts li { display: flex; align-items: center; gap: 10px; font-size: 13px; font-weight: 300; color: var(--ink); line-height: 22px; }
  .contacts svg { width: 11px; height: 11px; fill: none; stroke: var(--violet); stroke-width: 1.6; flex: none; }
  .contacts .accent { color: var(--violet); }

  .address { position: absolute; right: 36px; top: 196px; text-align: right; font-size: 13px; font-weight: 300; color: var(--ink); line-height: 22px; font-style: normal; }
</style>
</head>
<body>
<main class="stage">
  <section class="card card--front" aria-label="Card front">
    <div class="brand">
      <span class="brand__mark"></span>
      <span class="brand__name">QUENDRA</span>
    </div>
  </section>

  <section class="card card--back" aria-label="Card back">
    <div class="brand">
      <span class="brand__mark"></span>
      <span class="brand__name">QUENDRA</span>
    </div>

    <div class="holder">
      <p class="holder__name">LUKAS MAREND</p>
      <p class="holder__role">Managing Partner</p>
    </div>

    <div class="divider"></div>

    <ul class="contacts">
      <li><svg viewBox="0 0 12 12"><path d="M2 1.5 L4 1.5 L5 4 L3.8 5 Q5 7.5 7 8.2 L8 7 L10.5 8 L10.5 10 Q6 11 2 5.5 Z"/></svg><span>+49 170 482 316 75</span></li>
      <li><svg viewBox="0 0 12 12"><rect x="1" y="2.5" width="10" height="7"/><path d="M1 2.5 L6 6.5 L11 2.5"/></svg><span>info@quendra.com</span></li>
      <li><svg viewBox="0 0 12 12"><circle cx="6" cy="6" r="5"/><path d="M1 6 H11 M6 1 Q3 6 6 11 Q9 6 6 1"/></svg><span>www.<span class="accent">quendra</span>.com</span></li>
    </ul>

    <address class="address">
      Lindenweg 12, 39100<br>
      Bolzano, Italy
    </address>
  </section>
</main>
</body>
</html>
```